Mira Tails

im a dog walker, pet sitter and dog groomer. I can look after all pets from once a day pop in feeds of cats to small holdings and exotics. have 10 years experience in the industry. I can look after peoples dogs for the day while they are out or for longer if on holiday. I walk dogs when people are at work so the dogs get to have fun too. I do house sitting so all your animals are looked after together. you have designed my business cards and I wanted the 'mira tails' with the paw to be the same on the leaflets. I have spoken to printolane and they have sent a pdf file of business card and said it can be cropped. please let me know if this cant be done
im also a qualified canine hydrotherapist

Target Market(s)

pet owners

Industry/Entity Type

Pet

Requirements
Must have
• my phone number 07834562719
• email miratails@mailbox-example.co.uk
• area; Tunbridge wells, Sevenoaks and surrounding areas
• I want it almost done as bullet points with the main things being the dog walking and the pet sitting.
Nice to have
• cartoon animals like business card not the cartoons with big eyes

```html
<!DOCTYPE html>
<html lang="en">
<head>
<meta charset="utf-8">
<title>Mira Tails – Dog Walker, Pet Sitter &amp; Dog Groomer</title>
<link rel="stylesheet" href="https://fonts.googleapis.com/css2?family=Montserrat:wght@600;700&family=Roboto+Condensed:wght@300;400&family=Tinos&display=swap">
<style>
  :root {
    --violet: #7b52e8;
    --violet-soft: #a98df0;
    --lilac: #d9ccf8;
    --white: #ffffff;
    --ink: #1d1d24;
    --cyan: #33bde8;
    --grass: #6fcf3a;
    --foliage: #2f4a1e;
    --stage: #efe9e2;
  }
  * { box-sizing: border-box; margin: 0; padding: 0; }
  html, body {
    width: 1200px; height: 1122px; overflow: hidden;
    background: var(--stage);
  }
  .leaflet {
    position: absolute; left: 222px; top: 24px;
    width: 756px; height: 1074px;
    background: linear-gradient(180deg, var(--violet-soft) 0%, var(--lilac) 22%, #f3eefd 38%, var(--white) 46%);
    box-shadow: 0 10px 30px rgba(60, 40, 20, 0.18);
    overflow: hidden;
  }
  .leaflet__headline {
    position: absolute; left: 40px; top: 30px;
    font-family: "Montserrat", sans-serif; font-weight: 700;
    font-size: 26px; letter-spacing: 1px; color: var(--white);
    text-transform: uppercase;
  }
  .leaflet__illustration {
    position: absolute; left: 108px; top: 96px;
    width: 556px; height: 356px;
    background: linear-gradient(180deg, var(--foliage) 0%, #4e7a2a 35%, var(--grass) 62%, #8ddf4e 100%);
  }
  .services {
    position: absolute; left: 108px; top: 488px;
    list-style: none;
    font-family: "Roboto Condensed", sans-serif; font-weight: 400;
    font-size: 27px; line-height: 1.22; color: var(--ink);
  }
  .services li { position: relative; padding-left: 30px; }
  .services li::before {
    content: ""; position: absolute; left: 4px; top: 12px;
    width: 12px; height: 12px; border-radius: 50%;
    background: var(--violet);
  }
  .services .indent { padding-left: 30px; }
  .services .indent::before { display: none; }
  .area {
    position: absolute; left: 0; right: 0; top: 762px; text-align: center;
    font-family: "Tinos", serif; font-size: 27px; color: var(--cyan);
  }
  .brand {
    position: absolute; left: 0; right: 0; top: 820px;
    display: flex; align-items: center; justify-content: center; gap: 18px;
  }
  .brand__dot { width: 60px; height: 60px; border-radius: 50%; background: var(--violet); }
  .brand__name {
    font-family: "Montserrat", sans-serif; font-weight: 600;
    font-size: 54px; color: var(--violet);
  }
  .experience {
    position: absolute; left: 0; right: 0; top: 912px; text-align: center;
    font-family: "Tinos", serif; font-size: 25px; color: var(--cyan);
  }
  .contact-bar {
    position: absolute; left: 0; right: 0; bottom: 0; height: 104px;
    background: var(--violet);
    display: flex; align-items: center; justify-content: center;
    font-family: "Roboto Condensed", sans-serif; font-weight: 300;
    font-size: 32px; color: var(--white); gap: 16px;
  }
</style>
</head>
<body>
  <main class="leaflet">
    <h1 class="leaflet__headline">Dog walker, pet sitter &amp; dog groomer</h1>
    <div class="leaflet__illustration" role="img" aria-label="Cartoon illustration of a brown dog, a grey cat, a rabbit and a hen sitting on a green lawn in front of dark foliage"></div>

    <ul class="services">
      <li>Dog walker, pet sitter &amp; dog groomer</li>
      <li>Pet / House sitting - can pop in to feed</li>
      <li class="indent">your pets or small holdings and exotics</li>
      <li>10 years experience</li>
      <li>Will sit pets a portion of the day, all day or all week!</li>
      <li>Ensure pets get exercise and fun</li>
      <li>Qualified canine hydrotherapist</li>
    </ul>

    <p class="area">Tunbridge Wells, Sevenoaks and surrounding areas</p>

    <div class="brand">
      <span class="brand__dot" aria-hidden="true"></span>
      <span class="brand__name">Mira Tails</span>
    </div>

    <p class="experience">10 years experience in animal industry</p>

    <footer class="contact-bar">
      <span class="contact-bar__phone">07834562719</span>
      <span aria-hidden="true">|</span>
      <span class="contact-bar__email">email miratails@mailbox-example.co.uk</span>
    </footer>
  </main>
</body>
</html>
```